Luminously Grounded Vitality

We want to design a business card that is modern and appealing for an innovative psychedelic telemedicine company that provides at-home ketamine-assisted therapy along with wellness, longevity, and anti-aging medicines. We want to use our deep purple and white plus other colors you can find on our website. We don't have any strict brand guidelines yet so feel free to get creative. We want a very professional, but technology first modern design that will instill trust, peace, calm, but also be attractive to investors in the healthcare and SaaS space.

```html
<!DOCTYPE html>
<html lang="en">
<head>
<meta charset="utf-8">
<title>Luminously Business Card</title>
<link rel="stylesheet" href="https://fonts.googleapis.com/css2?family=Montserrat:wght@400;500;700&display=swap">
<style>
  :root {
    --backdrop: #e9e6ee;
    --card-white: #ffffff;
    --purple-deep: #6c559f;
    --purple-mid: #8a74bd;
    --purple-light: #a896d2;
    --purple-faint: #ece7f5;
    --text-grey: #4a4458;
  }
  * { box-sizing: border-box; margin: 0; padding: 0; }
  html, body {
    width: 900px; height: 1200px; overflow: hidden;
    background: var(--backdrop);
    font-family: "Montserrat", sans-serif;
  }
  .canvas { position: relative; width: 900px; height: 1200px; }
  .card {
    position: absolute; left: 100px; width: 700px; height: 420px;
    border-radius: 26px; overflow: hidden;
    box-shadow: 0 10px 28px rgba(60, 40, 90, 0.18);
  }
  .card-front { top: 120px; background: var(--card-white); }
  .card-back {
    top: 650px;
    background: linear-gradient(135deg, var(--purple-light) 0%, var(--purple-mid) 55%, var(--purple-deep) 100%);
  }
  .front-decor {
    position: absolute; left: 30px; top: -30px; width: 230px; height: 230px;
    border-radius: 50%; background: var(--purple-faint);
  }
  .brand-lockup {
    position: absolute; right: 50px; top: 40px; width: 230px;
    display: flex; flex-direction: column; align-items: center; gap: 14px;
  }
  .brand-dot { width: 64px; height: 64px; border-radius: 50%; background: var(--purple-mid); }
  .brand-name {
    font-weight: 400; font-size: 36px; color: var(--purple-deep); letter-spacing: 0.5px;
  }
  .person { position: absolute; left: 40px; top: 228px; }
  .person-name { font-weight: 700; font-size: 26px; color: var(--purple-deep); }
  .person-role { font-weight: 500; font-size: 15px; color: var(--text-grey); margin-top: 4px; }
  .divider {
    position: absolute; left: 40px; right: 40px; top: 300px;
    height: 2px; background: var(--purple-mid);
  }
  .contact-list {
    position: absolute; left: 40px; top: 318px; list-style: none;
    display: flex; flex-direction: column; gap: 8px;
  }
  .contact-item {
    display: flex; align-items: center; gap: 10px;
    font-size: 15px; color: var(--text-grey);
  }
  .contact-icon { width: 16px; height: 16px; flex: none; }
  .address {
    position: absolute; right: 40px; top: 326px; text-align: right;
    font-style: normal; font-size: 15px; line-height: 1.5; color: var(--text-grey);
  }
  .back-decor {
    position: absolute; left: -40px; top: 40px; width: 330px; height: 330px;
    border-radius: 50%; background: rgba(255, 255, 255, 0.14);
  }
  .back-brand {
    position: absolute; right: 44px; top: 262px;
    font-weight: 400; font-size: 44px; color: var(--card-white); letter-spacing: 0.5px;
  }
</style>
</head>
<body>
<main class="canvas">
  <section class="card card-front" aria-label="Business card front">
    <div class="front-decor" aria-hidden="true"></div>
    <div class="brand-lockup">
      <span class="brand-dot" aria-hidden="true"></span>
      <span class="brand-name">Luminously</span>
    </div>
    <div class="person">
      <h1 class="person-name">Clara Venturini</h1>
      <p class="person-role">Co-Founder</p>
    </div>
    <div class="divider" aria-hidden="true"></div>
    <ul class="contact-list">
      <li class="contact-item">
        <svg class="contact-icon" viewBox="0 0 24 24" aria-hidden="true"><path fill="#6c559f" d="M6.6 10.8a15.1 15.1 0 0 0 6.6 6.6l2.2-2.2a1 1 0 0 1 1-.25 11.4 11.4 0 0 0 3.6.57 1 1 0 0 1 1 1V20a1 1 0 0 1-1 1A17 17 0 0 1 3 4a1 1 0 0 1 1-1h3.5a1 1 0 0 1 1 1c0 1.25.2 2.45.57 3.57a1 1 0 0 1-.25 1z"/></svg>
        833-555-0142
      </li>
      <li class="contact-item">
        <svg class="contact-icon" viewBox="0 0 24 24" aria-hidden="true"><rect x="2" y="5" width="20" height="14" rx="2" fill="#6c559f"/><path d="M3 6l9 7 9-7" fill="none" stroke="#fff" stroke-width="1.8"/></svg>
        info@luminously.com
      </li>
      <li class="contact-item">
        <svg class="contact-icon" viewBox="0 0 24 24" aria-hidden="true"><circle cx="12" cy="12" r="9.5" fill="none" stroke="#6c559f" stroke-width="2"/><path d="M2.5 12h19M12 2.5c3 3 3 16 0 19M12 2.5c-3 3-3 16 0 19" fill="none" stroke="#6c559f" stroke-width="1.6"/></svg>
        www.luminously.com
      </li>
    </ul>
    <address class="address">Lindenweg 42<br>22769 Hamburg</address>
  </section>

  <section class="card card-back" aria-label="Business card back">
    <div class="back-decor" aria-hidden="true"></div>
    <span class="back-brand">Luminously</span>
  </section>
</main>
</body>
</html>
```